Talvora Cellars WIX website

We are opening a new winery called Talvora Cellars. We think that "Wine should be an experience..." To aid in that experience, each bottle of wine label will have a unique QR code that directs patrons to a page on the site that highlights the wines. On this page each wine bottle will be displayed, the winemaking notes will be included. Also included will be food pairings with recipes, movie and music ideas and anything else that will add to the experience. I need a website that helps showcase annual wines, has a members only area (for the wine club) and allows people to purchase wine on-line. I've started the beginning of a site on WIX - talvoracellars-demo.com. There's no requirement or expectation to simply finish what I've started. I just needed to get something up and live. Let your imagination take over. I want to unique site and kicks a*s...
Updates

Logo font is Trajan Pro...

I'm open to any designs, meaning don't feel like you have to complete what I started.

I want to keep the logo and the font, however...

Other fonts used should compliment Trajan Pro.

Font styles to use
Serif
Other font styles liked:
• Trajan Pro is what was used for the logo

Requirements
Must have
• Attractive and compelling home page, red wine section, white wine section, members only area, page that speaks of and allows purchase into a wine club, all easy enough for me to edit and add pages without coding knowledge. Adding pages is why I chose WIX as the platform. Here is a list of the pages or tabs: About, Events, Vintner’s Circle, Press/Accolades, Wines - Red/White/Dessert/Summer Series (as sub pages), Contact

```html
<!DOCTYPE html>
<html lang="en">
<head>
<meta charset="utf-8">
<title>Talvora Cellars</title>
<link rel="stylesheet" href="https://fonts.googleapis.com/css2?family=Cinzel:wght@400;500;600&display=swap">
<style>
:root{
  --bg:#08090b;
  --panel:#0c0d10;
  --ink:#e6e2d8;
  --muted:#8d8a82;
  --gold:#c9a54a;
  --amber:#c8741d;
  --note:#b07a3c;
  --olive:#5e4f0c;
  --rule:#7d7a73;
  --field:#ffffff;
}
*{box-sizing:border-box;margin:0;padding:0}
html,body{width:1171px;height:1200px;overflow:hidden;background:var(--bg)}
body{position:relative;font-family:"Cinzel",serif;color:var(--ink)}
.abs{position:absolute}
.nav{position:absolute;display:flex;align-items:center;justify-content:center;gap:16px;border-top:1px solid var(--rule);border-bottom:1px solid var(--rule);font-size:8.5px;letter-spacing:.3px;white-space:nowrap}
.nav-left{left:247px;top:81px;width:203px;height:28px}
.nav-right{left:720px;top:87px;width:202px;height:27px;gap:11px;font-size:8px}
.brand-mark{position:absolute;display:flex;flex-direction:column;align-items:center;justify-content:center;gap:3px;color:var(--ink);font-weight:400;text-align:center;line-height:1.05}
.brand-mark .dot{width:7px;height:7px;border:1px solid var(--ink)}
.brand-header{left:544px;top:62px;width:80px;height:64px;font-size:11px}
.contact-chip{position:absolute;text-align:center;font-size:6px;color:var(--muted);letter-spacing:.3px;white-space:nowrap}
.contact-chip svg{display:block;margin:0 auto 4px}
.hero{position:absolute;left:221px;top:170px;width:729px;height:255px}
.hero-photo{position:absolute;inset:0}
.hero-copy{position:absolute;left:0;right:0;top:96px;text-align:center}
.hero-kicker{font-size:19px;color:#f4efe3;letter-spacing:.5px}
.hero-title{font-size:30px;color:var(--gold);font-weight:500;line-height:1.1;letter-spacing:.5px}
.hero-text{width:360px;margin:14px auto 0;font-size:7.6px;line-height:1.45;color:#f1ead8}
.btn-read{position:absolute;left:314px;top:202px;width:88px;height:23px;background:#0b0b0b;border:1px solid #3a3220;color:var(--gold);font-size:7.5px;display:flex;align-items:center;justify-content:center}
.maker-photo{position:absolute;left:271px;top:435px;width:259px;height:182px}
.maker-panel{position:absolute;left:585px;top:435px;width:365px;height:194px;background:var(--panel)}
.maker-title{position:absolute;left:42px;top:63px;font-size:15.5px;color:var(--amber);letter-spacing:.3px;font-weight:400;white-space:nowrap}
.maker-note{position:absolute;left:42px;top:88px;width:290px;font-size:6.6px;line-height:1.5;color:var(--note)}
.divider{position:absolute;left:585px;top:698px;width:1px;height:264px;background:#3a3a3a}
.brand-contact{left:390px;top:752px;width:68px;height:66px;font-size:10px}
.contact-lines{position:absolute;left:290px;top:826px;width:268px;text-align:center;font-size:9px;line-height:21px;color:#e9e6df;white-space:nowrap}
.contact-lines svg{vertical-align:-1px;margin-right:3px}
.form-title{position:absolute;left:650px;top:695px;width:160px;text-align:center;font-size:14px;color:#e6e2d8;font-weight:400}
.label{position:absolute;left:601px;font-size:8.5px;color:var(--muted)}
.field{position:absolute;left:669px;width:219px;background:var(--field);border-radius:2px;font-size:8.5px;color:#8a8a8a;padding:0 7px;display:flex;align-items:center}
.field.select{color:#111;justify-content:space-between}
.field.area{align-items:flex-start;padding-top:11px}
.btn-submit{position:absolute;left:669px;top:948px;width:104px;height:15px;background:var(--olive);color:#15130a;font-size:8px;display:flex;align-items:center;justify-content:center}
.brand-footer{left:318px;top:1048px;width:102px;height:100px;font-size:14px}
.foot-head{position:absolute;font-size:13.5px;color:#e6e2d8;line-height:1.3;font-weight:400}
.foot-item{position:absolute;font-size:5.8px;color:#d8d4ca;line-height:1.35}
.foot-item svg{vertical-align:-1px;margin-right:4px}
.foot-menu{position:absolute;left:660px;top:1069px;font-size:6.5px;line-height:12.5px;color:#d8d4ca;list-style:none;white-space:nowrap}
.social{position:absolute;top:1095px;width:15px;height:15px;border:1.6px solid #ffffff;border-radius:50%}
</style>
</head>
<body>

<nav class="nav nav-left"><span>About Us</span><span>Events</span><span>Wines</span></nav>
<div class="brand-mark brand-header"><span class="dot"></span><span>Talvora</span><span>Cellars</span></div>
<nav class="nav nav-right"><span>Vintner’s Circle</span><span>Members</span><span>Contact Us</span></nav>

<div class="contact-chip" style="left:482px;top:132px;width:70px">
  <svg width="15" height="15" viewBox="0 0 16 16"><circle cx="8" cy="8" r="7" fill="none" stroke="#e6e2d8"/><path d="M5.6 4.6l1.3-.3.8 1.8-.8.7a5 5 0 0 0 2.3 2.3l.7-.8 1.8.8-.3 1.3c-2.8.4-6.2-3-5.8-5.8z" fill="#e6e2d8"/></svg>
  +61 2 5550 0142
</div>
<div class="contact-chip" style="left:592px;top:132px;width:120px">
  <svg width="15" height="15" viewBox="0 0 16 16"><circle cx="8" cy="8" r="7" fill="none" stroke="#e6e2d8"/><rect x="4.5" y="5.5" width="7" height="5" fill="#e6e2d8"/><path d="M4.5 5.5l3.5 2.7 3.5-2.7" fill="none" stroke="#08090b" stroke-width=".8"/></svg>
  hello@talvoracellars-demo.com
</div>

<div class="abs" style="left:221px;top:168px;width:729px;height:1px;background:#4a3a1e"></div>

<section class="hero">
  <svg class="hero-photo" role="img" aria-label="Photograph of a glass of golden wine on a bar counter with warm blurred lights" width="729" height="255" viewBox="0 0 729 255">
    <defs>
      <linearGradient id="heroFill" x1="0" y1="0" x2="0" y2="1">
        <stop offset="0" stop-color="#6a4a2a"/>
        <stop offset=".35" stop-color="#3b4660"/>
        <stop offset=".6" stop-color="#6b5120"/>
        <stop offset="1" stop-color="#2a1c0c"/>
      </linearGradient>
      <radialGradient id="heroGlow" cx=".55" cy=".55" r=".5">
        <stop offset="0" stop-color="#d9a640" stop-opacity=".65"/>
        <stop offset="1" stop-color="#d9a640" stop-opacity="0"/>
      </radialGradient>
    </defs>
    <path d="M0 0H729V187C600 205 500 245 330 253C200 258 60 250 0 232Z" fill="url(#heroFill)"/>
    <path d="M0 0H729V187C600 205 500 245 330 253C200 258 60 250 0 232Z" fill="url(#heroGlow)"/>
    <path d="M0 232C60 250 200 258 330 253C500 245 600 205 729 187" fill="none" stroke="#b8902e" stroke-width="2"/>
  </svg>
  <div class="hero-copy">
    <div class="hero-kicker">Welcome to</div>
    <div class="hero-title">Talvora Cellars</div>
    <p class="hero-text">We believe that everyone deserves to have great tasting and high quality wine. That is why after more than 10 years of experience, we decided to open an online store.</p>
  </div>
  <div class="btn-read">Read more</div>
</section>

<svg class="maker-photo" role="img" aria-label="Black and white portrait of the winemaker tasting red wine" viewBox="0 0 259 182">
  <defs>
    <radialGradient id="makerFill" cx=".5" cy=".45" r=".6">
      <stop offset="0" stop-color="#9a9a9a"/>
      <stop offset=".7" stop-color="#4a4a4a"/>
      <stop offset="1" stop-color="#08090b"/>
    </radialGradient>
  </defs>
  <rect width="259" height="182" fill="url(#makerFill)"/>
</svg>

<section class="maker-panel">
  <h2 class="maker-title">A Message from the Winemaker</h2>
  <p class="maker-note">I started my winemaking journey with one simple goal in mind - I wanted to make wine as good or better than the wine I could buy. At the time of that goal in 2015, I had no perspective on the path that would form before me.<br>I'm excited for you to try my wine. Pair it with the food ideas. Follow the recipes; listen to the music.<br>Enjoy...the experience.<br>--Elias Talvora--</p>
</section>

<div class="divider"></div>

<div class="brand-mark brand-contact"><span class="dot"></span><span>Talvora</span><span>Cellars</span></div>
<div class="contact-lines">
  <div><svg width="9" height="9" viewBox="0 0 16 16"><path d="M3 1l3-.5 2 4-2 1.6a9 9 0 0 0 4 4l1.6-2 4 2-.5 3C8 14.5 1.5 8 3 1z" fill="#e9e6df"/></svg>+61 2 5550 0142</div>
  <div><svg width="9" height="8" viewBox="0 0 16 12"><rect width="16" height="12" fill="#e9e6df"/><path d="M0 0l8 6 8-6" fill="none" stroke="#08090b" stroke-width="1.3"/></svg>hello@talvoracellars-demo.com</div>
  <div>Harbour Lane, Northcove NSW 2999, Australia</div>
  <div>PO Box 208: Ridgefell SA 5999, Australia</div>
</div>

<h2 class="form-title">Contact Us</h2>
<span class="label" style="top:734px">First Name</span>
<div class="field" style="top:726px;height:25px">Your name..</div>
<span class="label" style="top:770px">Last Name</span>
<div class="field" style="top:763px;height:25px">Your last name..</div>
<span class="label" style="top:805px">Country</span>
<div class="field select" style="top:801px;height:22px"><span>Australia</span><svg width="7" height="5" viewBox="0 0 7 5"><path d="M1 1l2.5 2.5L6 1" fill="none" stroke="#111" stroke-width="1.3"/></svg></div>
<span class="label" style="top:888px">Subject</span>
<div class="field area" style="top:834px;height:104px">Write something..</div>
<div class="btn-submit">Submit</div>

<div class="brand-mark brand-footer"><span class="dot"></span><span>Talvora</span><span>Cellars</span></div>

<h3 class="foot-head" style="left:510px;top:1044px">Address</h3>
<div class="foot-item" style="left:510px;top:1072px"><svg width="6" height="6" viewBox="0 0 16 16"><path d="M3 1l3-.5 2 4-2 1.6a9 9 0 0 0 4 4l1.6-2 4 2-.5 3C8 14.5 1.5 8 3 1z" fill="#d8d4ca"/></svg>+61 2 5550 0142</div>
<div class="foot-item" style="left:510px;top:1088px"><svg width="6" height="5" viewBox="0 0 16 12"><rect width="16" height="12" fill="#d8d4ca"/><path d="M0 0l8 6 8-6" fill="none" stroke="#08090b" stroke-width="1.5"/></svg>hello@talvoracellars-demo.com</div>
<div class="foot-item" style="left:510px;top:1104px;width:100px">Harbour Lane, Northcove NSW 2999, Australia</div>
<div class="foot-item" style="left:510px;top:1128px;width:100px">PO Box 208: Ridgefell SA 5999, Australia</div>

<h3 class="foot-head" style="left:660px;top:1043px;font-size:10px">Menu</h3>
<ul class="foot-menu">
  <li>About Us</li><li>Events</li><li>Wines</li><li>Vintner’s Circle</li><li>Members</li><li>Contact Us</li>
</ul>

<h3 class="foot-head" style="left:810px;top:1044px">Social<br>Media</h3>
<span class="social" style="left:810px" aria-label="Social profile one"></span>
<span class="social" style="left:835px" aria-label="Social profile two"></span>
<span class="social" style="left:860px" aria-label="Social profile three"></span>

</body>
</html>
```